Pathways to Brightmoor Land Ventures

size of the ad - 8”x 10.75" plus 0.25" bleed
I would like an ad for a magazine that will stand out and make people want to read the ad.
The ad should not be crowded and people reading the ad will be able to read the text.
I would like it to be a creative and modern-day design.
the list of topics should not be the focus of the ad.
the text is attached.
If you decide to use people in the ad then please no ladies.
please note that leave over 1 inch for the bottom of the footer

```html
<!DOCTYPE html>
<html lang="en">
<head>
<meta charset="UTF-8">
<title>Real Estate Course – Pathways to Brightmoor Land Ventures</title>
<link href="https://fonts.googleapis.com/css2?family=Montserrat:wght@400;500;600;700;800;900&display=swap" rel="stylesheet">
<style>
  :root{
    --navy:#0e2a47;
    --teal:#1c6f8c;
    --sky:#bfe7f4;
    --sky-deep:#7fcbe6;
    --ink:#1b2633;
    --white:#ffffff;
    --page:#e9edf0;
  }
  *{box-sizing:border-box;margin:0;padding:0}
  html,body{width:710px;height:1200px;overflow:hidden;background:var(--page)}
  body{font-family:"Montserrat",Arial,sans-serif;color:var(--ink)}
  .ad{position:relative;width:710px;height:1200px;background:var(--white);overflow:hidden}
  .hero-photo{
    position:absolute;left:0;top:0;width:710px;height:640px;
    background:
      radial-gradient(ellipse 260px 320px at 560px 210px,rgba(255,170,90,.9),rgba(240,110,60,.35) 45%,transparent 70%),
      linear-gradient(100deg,#0f2a3d 0%,#1f4a63 28%,#2d6d88 45%,#3a5a6e 60%,#8a4f3a 78%,#3b3440 100%);
  }
  .hero-fade{
    position:absolute;left:0;top:380px;width:710px;height:460px;
    background:linear-gradient(180deg,rgba(191,231,244,0) 0%,rgba(191,231,244,.85) 45%,var(--sky) 62%,rgba(255,255,255,1) 100%);
  }
  .logo{
    position:absolute;left:38px;top:34px;width:124px;height:124px;background:var(--white);
    display:flex;align-items:center;justify-content:center;
    font-weight:800;font-size:15px;letter-spacing:.5px;color:var(--navy);
  }
  .title{
    position:absolute;left:36px;top:560px;width:650px;
    font-weight:900;font-size:84px;line-height:.88;letter-spacing:-1px;color:var(--navy);
    text-transform:uppercase;
  }
  .title .row{display:block}
  .title .row--two{padding-left:2px}
  .title-rule{position:absolute;left:36px;top:724px;width:638px;height:3px;background:var(--navy)}
  .intro{position:absolute;left:36px;top:752px;width:320px}
  .intro__name{font-weight:800;font-size:27px;line-height:1.08;color:var(--navy);text-transform:uppercase}
  .intro__tag{margin-top:24px;font-weight:800;font-size:23px;line-height:1.1;color:var(--teal);text-transform:uppercase}
  .schedule{position:absolute;left:36px;top:990px;width:320px}
  .schedule__place{display:inline-block;background:var(--navy);color:var(--white);font-weight:700;font-size:20px;padding:6px 14px}
  .schedule__row{display:flex;justify-content:space-between;margin-top:10px}
  .schedule__when{font-size:15px;line-height:1.15;color:var(--navy);font-weight:600}
  .schedule__when b{font-size:26px;font-weight:800;margin-right:6px;vertical-align:-3px}
  .schedule__start{font-size:15px;font-weight:600;color:var(--navy);line-height:1.15}
  .schedule__start b{display:block;font-size:22px;font-weight:800}
  .topics{position:absolute;left:392px;top:752px;width:290px}
  .topics__head{font-weight:800;font-size:22px;color:var(--navy)}
  .topics__sub{font-weight:700;font-size:17px;color:var(--teal);margin-top:2px}
  .topics__list{list-style:none;display:grid;grid-template-columns:1fr 1fr;column-gap:16px;row-gap:9px;margin-top:16px}
  .topics__list li{position:relative;padding-left:12px;font-size:12px;line-height:1.25;color:var(--ink)}
  .topics__list li::before{content:"";position:absolute;left:0;top:5px;width:5px;height:5px;border-radius:50%;background:var(--teal)}
  .contact{display:flex;gap:18px;margin-top:22px;font-size:12px;font-weight:600;color:var(--navy)}
  .contact span{display:flex;align-items:center;gap:6px}
  .contact svg{width:16px;height:16px}
  .offer{margin-top:18px;font-size:12px;line-height:1.4;color:var(--ink)}
  .offer strong{display:block;font-weight:700;color:var(--navy)}
</style>
</head>
<body>
<main class="ad">
  <div class="hero-photo" role="img" aria-label="Upward view of glass skyscrapers with warm sunlight flaring between the towers"></div>
  <div class="hero-fade"></div>

  <div class="logo">BRIGHTMOOR</div>

  <h1 class="title"><span class="row">Real Estate</span><span class="row row--two">Course</span></h1>
  <div class="title-rule"></div>

  <section class="intro">
    <h2 class="intro__name">Pathways to Brightmoor Land Ventures</h2>
    <p class="intro__tag">Investing in knowledge is investing in opportunities</p>
  </section>

  <section class="schedule">
    <span class="schedule__place">Ridgefield</span>
    <div class="schedule__row">
      <p class="schedule__when"><b>10</b>Tuesday<br>Evenings Sessions</p>
      <p class="schedule__start">Starting<b>February 28</b></p>
    </div>
  </section>

  <section class="topics">
    <h3 class="topics__head">TOPICS</h3>
    <p class="topics__sub">Partial Listing</p>
    <ul class="topics__list">
      <li>Real estate investment strategies</li>
      <li>Real estate legal basics</li>
      <li>Due diligence</li>
      <li>Dealing with brokers</li>
      <li>Financing</li>
      <li>Sourcing deals</li>
      <li>Underwriting</li>
      <li>Syndication</li>
      <li>Property management</li>
      <li>Tax fundamentals</li>
    </ul>
    <div class="contact">
      <span><svg viewBox="0 0 24 24" fill="none" stroke="currentColor" stroke-width="2"><path d="M5 3h4l2 5-3 2a11 11 0 0 0 6 6l2-3 5 2v4a2 2 0 0 1-2 2A17 17 0 0 1 3 5a2 2 0 0 1 2-2z"/></svg>555-014-2276</span>
      <span><svg viewBox="0 0 24 24" fill="none" stroke="currentColor" stroke-width="2"><circle cx="12" cy="12" r="9"/><path d="M3 12h18M12 3c3 3 3 15 0 18M12 3c-3 3-3 15 0 18"/></svg>www.brightmoorland.com</span>
    </div>
    <p class="offer">Limited Partial Scholarships<strong>Early Bird Special</strong>For those that started or would like to go into real estate</p>
  </section>
</main>
</body>
</html>
```